Criação de Kit com 5 Layouts de Post para Redes Sociais (Facebook, Instagram e etc) para Consultoria de Negócios
" EVENTO DE DOIS DIAS COM VÁRIOS PALESTRANTES, TRAZENDO CONHECIMENTO EM VARIAS ÁREAS PARA AS MULHERES EMPREENDEDORAS. UM EVENTO DE IMERSSAO DE 19 HORAS. "

```html
<!DOCTYPE html>
<html lang="pt-BR">
<head>
<meta charset="UTF-8">
<title>Fortalecimento Pessoal e Profissional</title>
<link href="https://fonts.googleapis.com/css2?family=Montserrat:wght@400;500;600;800&display=swap" rel="stylesheet">
<style>
  :root {
    --pink-light: #f4c3ca;
    --pink-mid: #eeaab5;
    --pink-deep: #e2909e;
    --plum: #3e0f2b;
    --plum-text: #4a1431;
    --gold: #d8b467;
    --gold-light: #f1d99a;
    --white: #ffffff;
    --photo-a: #f1c9c6;
    --photo-b: #e7b3b4;
  }
  html, body {
    margin: 0;
    padding: 0;
    width: 1200px;
    height: 1200px;
    overflow: hidden;
  }
  .post {
    position: relative;
    width: 1200px;
    height: 1200px;
    overflow: hidden;
    background: linear-gradient(135deg, var(--pink-light) 0%, var(--pink-mid) 55%, var(--pink-deep) 100%);
    font-family: "Montserrat", Arial, sans-serif;
  }
  .portrait {
    position: absolute;
    left: 96px;
    top: 0;
    width: 610px;
    height: 900px;
    border-radius: 300px 300px 0 0;
    background: radial-gradient(ellipse at 50% 35%, var(--photo-a) 0%, var(--photo-b) 70%, rgba(231,179,180,0) 100%);
  }
  .headline {
    position: absolute;
    left: 652px;
    top: 102px;
    color: var(--plum-text);
    line-height: 1;
    margin: 0;
  }
  .headline span { display: block; white-space: nowrap; }
  .headline .line-top { font-size: 45px; font-weight: 500; letter-spacing: 0.5px; }
  .headline .line-main { font-size: 84px; font-weight: 800; letter-spacing: 1px; margin-top: 8px; }
  .headline .line-bottom { font-size: 45px; font-weight: 500; letter-spacing: 0.5px; margin-top: 8px; }
  .headline-rule {
    position: absolute;
    left: 652px;
    top: 336px;
    width: 120px;
    height: 6px;
    background: var(--white);
  }
  .footer-shape {
    position: absolute;
    left: 0;
    top: 0;
    width: 1200px;
    height: 1200px;
  }
  .brand {
    position: absolute;
    left: 52px;
    top: 965px;
    display: flex;
    align-items: center;
    gap: 26px;
  }
  .brand-mark {
    width: 150px;
    height: 150px;
    border-radius: 50%;
    border: 5px solid var(--gold);
    box-sizing: border-box;
  }
  .brand-name {
    color: var(--gold);
    font-size: 92px;
    font-weight: 500;
    letter-spacing: 4px;
  }
  .contact {
    position: absolute;
    left: 612px;
    top: 1072px;
    color: var(--white);
    white-space: nowrap;
  }
  .contact-label {
    font-size: 24px;
    font-weight: 500;
    letter-spacing: 0.5px;
    margin-bottom: 12px;
  }
  .contact-row {
    display: flex;
    align-items: center;
    gap: 30px;
    font-size: 24px;
    font-weight: 400;
  }
  .contact-item { display: flex; align-items: center; gap: 10px; white-space: nowrap; }
  .contact-icon {
    flex: none;
    width: 26px;
    height: 26px;
    border-radius: 50%;
    background: var(--gold);
    display: flex;
    align-items: center;
    justify-content: center;
  }
</style>
</head>
<body>
<div class="post">
  <div class="portrait" role="img" aria-label="Fotografia de uma mulher de blusa rosa clara, mão no queixo, sorrindo"></div>

  <h1 class="headline">
    <span class="line-top">FORTALECIMENTO</span>
    <span class="line-main">PESSOAL</span>
    <span class="line-bottom">E PROFISSIONAL</span>
  </h1>
  <div class="headline-rule"></div>

  <svg class="footer-shape" viewBox="0 0 1200 1200" aria-hidden="true">
    <path d="M0 830 C 300 790 640 860 960 960 C 1060 990 1140 990 1200 975 L1200 1200 L0 1200 Z" fill="#3e0f2b"/>
    <path d="M720 1010 C 900 1030 1060 1010 1200 960 L1200 1000 C 1060 1040 900 1045 720 1010 Z" fill="#f0b7c0" opacity="0.55"/>
    <path d="M60 800 C 380 740 700 860 1030 1015 C 720 885 400 790 60 808 Z" fill="#d8b467"/>
    <path d="M60 800 C 380 740 700 860 1030 1015 C 760 880 430 775 60 803 Z" fill="#f1d99a" opacity="0.8"/>
  </svg>

  <div class="brand">
    <div class="brand-mark"></div>
    <div class="brand-name">AURA</div>
  </div>

  <div class="contact">
    <div class="contact-label">CONTATO:</div>
    <div class="contact-row">
      <div class="contact-item">
        <span class="contact-icon">
          <svg width="15" height="15" viewBox="0 0 24 24"><path d="M6.6 10.8a15.1 15.1 0 0 0 6.6 6.6l2.2-2.2a1 1 0 0 1 1-.25 11.4 11.4 0 0 0 3.6.57 1 1 0 0 1 1 1V20a1 1 0 0 1-1 1A17 17 0 0 1 3 4a1 1 0 0 1 1-1h3.5a1 1 0 0 1 1 1c0 1.25.2 2.45.57 3.57a1 1 0 0 1-.25 1z" fill="#3e0f2b"/></svg>
        </span>
        <span>(00) 0000-0000</span>
      </div>
      <div class="contact-item">
        <span class="contact-icon">
          <svg width="15" height="15" viewBox="0 0 24 24"><rect x="3" y="6" width="18" height="12" rx="1.5" fill="#3e0f2b"/><path d="M3.5 7l8.5 6 8.5-6" stroke="#d8b467" stroke-width="1.8" fill="none"/></svg>
        </span>
        <span>email@email.com.br</span>
      </div>
    </div>
  </div>
</div>
</body>
</html>
```